Reed & Vale NC grand opening (for BILLBOARD)

Advertising the grand opening of our cannabis/hemp shop in NC. We will sell all things hemp (flower, cartridges, disposables, edibles, creams, lotions, pet products etc...)

Requirements
Must have
• include, open starting Aug 1, but grand opening Aug 15th.
Nice to have
• Difference slogan ideas "Save some cash, buy our grass" "Find your perfect high at Reed & Vale cannabis store" "Experience Nature's Gift: Reed & Vale Cannabis Store"

```html
<!DOCTYPE html>
<html lang="en">
<head>
<meta charset="utf-8">
<title>Reed &amp; Vale — Grand Opening Billboard</title>
<link href="https://fonts.googleapis.com/css2?family=Anton&family=Montserrat:wght@700;800&family=Kaushan+Script&display=swap" rel="stylesheet">
<style>
  :root {
    --page-bg: #ffffff;
    --panel-white: #ffffff;
    --green-light: #8fdc55;
    --green-mid: #6cc93a;
    --green-deep: #4fa523;
    --brand-green: #6cbf3a;
    --navy: #111544;
    --edge-grey: #c9cbd6;
    --photo-warm: #efe6dd;
  }
  * { box-sizing: border-box; margin: 0; padding: 0; }
  html, body {
    width: 1000px;
    height: 1200px;
    overflow: hidden;
    background: var(--page-bg);
  }
  .canvas {
    position: relative;
    width: 1000px;
    height: 1200px;
  }
  .billboard {
    position: absolute;
    left: 50px;
    top: 412px;
    width: 900px;
    height: 375px;
    background: var(--panel-white);
    box-shadow: 0 6px 24px rgba(0, 0, 0, 0.18);
    overflow: hidden;
  }
  .billboard__art {
    position: absolute;
    inset: 0;
    width: 100%;
    height: 100%;
  }
  .brand-name {
    position: absolute;
    left: 23px;
    top: 30px;
    width: 220px;
    font-family: "Montserrat", sans-serif;
    font-weight: 800;
    font-size: 44px;
    line-height: 1.18;
    color: var(--brand-green);
    text-align: center;
    display: flex;
    flex-direction: column;
    align-items: center;
    gap: 8px;
  }
  .brand-name__dot {
    width: 20px;
    height: 20px;
    border-radius: 50%;
    background: var(--brand-green);
  }
  .headline-grand {
    position: absolute;
    left: 412px;
    top: 14px;
    font-family: "Kaushan Script", cursive;
    font-size: 80px;
    line-height: 1.25;
    color: #ffffff;
    -webkit-text-stroke: 3px var(--green-mid);
    paint-order: stroke fill;
    white-space: nowrap;
  }
  .headline-opening {
    position: absolute;
    left: 459px;
    top: 94px;
    width: 336px;
    font-family: "Anton", sans-serif;
    font-size: 88px;
    line-height: 1;
    letter-spacing: 1px;
    color: var(--navy);
    text-align: center;
    transform: scaleX(1.18);
    transform-origin: center;
  }
  .headline-rule {
    position: absolute;
    left: 418px;
    top: 189px;
    width: 433px;
    height: 2px;
    background: linear-gradient(90deg, rgba(17,21,68,0), rgba(17,21,68,0.55) 20%, rgba(17,21,68,0.55) 80%, rgba(17,21,68,0));
  }
  .location-exit {
    position: absolute;
    left: 525px;
    top: 228px;
    width: 363px;
    font-family: "Montserrat", sans-serif;
    font-weight: 800;
    font-size: 28px;
    line-height: 1;
    letter-spacing: 2px;
    color: var(--navy);
    text-align: center;
  }
  .location-exit__num { font-size: 36px; }
  .location-road {
    position: absolute;
    left: 525px;
    top: 270px;
    width: 363px;
    height: 42px;
    border-radius: 21px;
    background: var(--navy);
    font-family: "Montserrat", sans-serif;
    font-weight: 800;
    font-size: 30px;
    line-height: 42px;
    letter-spacing: 1px;
    color: #ffffff;
    text-align: center;
  }
  .opening-dates {
    position: absolute;
    left: 505px;
    top: 326px;
    width: 403px;
    font-family: "Montserrat", sans-serif;
    font-weight: 800;
    font-size: 17px;
    line-height: 1.2;
    letter-spacing: 1px;
    color: var(--navy);
    text-align: center;
  }
</style>
</head>
<body>
<main class="canvas">
  <section class="billboard" aria-label="Reed &amp; Vale grand opening billboard">
    <svg class="billboard__art" viewBox="0 0 900 375">
      <defs>
        <radialGradient id="green-field" cx="0.62" cy="0.42" r="0.75">
          <stop offset="0" stop-color="#8fdc55"/>
          <stop offset="0.6" stop-color="#6cc93a"/>
          <stop offset="1" stop-color="#4fa523"/>
        </radialGradient>
        <linearGradient id="promoter-tones" x1="0" y1="0" x2="1" y2="0">
          <stop offset="0" stop-color="#e9ddd2"/>
          <stop offset="0.55" stop-color="#efe6dd"/>
          <stop offset="0.8" stop-color="#d9c9c0"/>
          <stop offset="1" stop-color="#f4f1ee"/>
        </linearGradient>
      </defs>
      <polygon class="edge-shadow" points="365,0 900,0 900,375 287,375" fill="#c9cbd6"/>
      <polygon class="green-field" points="369,0 900,0 900,375 292,375" fill="url(#green-field)"/>
      <g class="accent-strokes" fill="#111544">
        <polygon points="688,58 736,40 692,63"/>
        <polygon points="700,46 718,36 703,49"/>
        <polygon points="430,318 447,333 434,320"/>
        <polygon points="436,312 450,319 438,314"/>
      </g>
      <rect class="promoter-photo" role="img"
            aria-label="Photo: excited young woman in a white tee shouting into a red and white megaphone"
            x="153" y="172" width="297" height="203" rx="6"
            fill="url(#promoter-tones)"/>
    </svg>

    <div class="brand-name">
      <span class="brand-name__dot" aria-hidden="true"></span>
      <span>Reed &amp;<br>Vale</span>
    </div>

    <h1 class="headline">
      <span class="headline-grand">Grand</span>
      <span class="headline-opening">OPENING</span>
    </h1>
    <div class="headline-rule" aria-hidden="true"></div>

    <p class="location-exit">OFF EXIT <span class="location-exit__num">6</span>A</p>
    <p class="location-road">BIRCHMONT RD</p>
    <p class="opening-dates">OPEN AUG 1 · GRAND OPENING AUG 15</p>
  </section>
</main>
</body>
</html>
```